User Interface Designer Needed

I need a few designs for a property law comparison website. We assist the public with finding a solicitor for the purchase or sale of their house and units. We are currently in the process of creating a questionnaire based woo commerce product filter using gravity forms. I'd like to see designs that use the logo colours. Users will be selecting options such as "Buying" or "Selling", they will then be selecting options such as "House" "Unit" or "Land". Details attached. The final design should communicate ease and simplicity. Questions will be answered one at a time, and the next question is dependent on the answer to the question prior

Target Market(s)

First home buyers, people from ages 18-80 make and female looking to get rid of the hassle of ringing around and going from website to website trying to get a quote

Industry/Entity Type

Real Estate

Number of Pages Required

1 page

Colors
33a6d7

Requirements
Must have
• A design for every question
Nice to have
• Simple symbols or simplistic pictures incorporated, even better if you can turn the question into a picture instead of words eg. A picture of a house, a picture of a unit and a picture of land instead of written answers

```html
<!DOCTYPE html>
<html lang="en">
<head>
<meta charset="utf-8">
<title>Keyvale – Property Type</title>
<link href="https://fonts.googleapis.com/css2?family=Open+Sans:wght@300;400;600;700&display=swap" rel="stylesheet">
<style>
:root{
  --brand:#06a6da;
  --ink:#333333;
  --muted:#c4c4c4;
  --rule:#dddddd;
  --back-bg:#e6e6e6;
  --footer-bg:#524f50;
  --white:#ffffff;
}
*{margin:0;padding:0;box-sizing:border-box}
html,body{width:1200px;height:1200px;overflow:hidden;background:var(--white)}
body{position:relative;font-family:"Open Sans",sans-serif;color:var(--ink)}
.brand{position:absolute;left:144px;top:46px;display:flex;align-items:center;gap:8px}
.brand-dot{width:34px;height:34px;border-radius:50%;background:var(--brand)}
.brand-name{font-size:28px;font-weight:700;color:var(--brand);letter-spacing:-.5px}
.nav{position:absolute;top:59px;left:0;width:100%;height:16px}
.nav a{position:absolute;font-size:11px;color:var(--ink);text-decoration:none;white-space:nowrap}
.nav .cart{top:2px}
.steps{position:absolute;left:350px;top:224px;width:472px;height:23px;border-bottom:1px solid var(--rule)}
.steps span{position:absolute;top:0;font-size:14px;color:var(--muted);white-space:nowrap}
.steps .current{color:var(--ink)}
.question{position:absolute;top:304px;left:0;width:1192px;text-align:center;font-size:38px;font-weight:300;color:var(--ink)}
.option{position:absolute;top:413px;width:134px;height:134px;border:2px solid var(--brand);border-radius:5px;background:var(--white);color:var(--brand)}
.option svg{position:absolute;left:50%;top:30px;transform:translateX(-50%)}
.option .label{position:absolute;left:0;right:0;top:102px;text-align:center;font-size:16px;font-weight:700;letter-spacing:-.6px;white-space:nowrap}
.option.selected{background:var(--brand);color:var(--white)}
.btn{position:absolute;top:619px;width:180px;height:52px;display:flex;align-items:center;justify-content:center;font-size:24px;font-weight:300}
.btn-back{left:398px;background:var(--back-bg);color:var(--ink)}
.btn-next{left:586px;background:var(--brand);color:var(--white)}
.testimonials{position:absolute;left:0;top:1027px;width:1200px;height:173px;background:var(--footer-bg);color:var(--white);text-align:center}
.testimonials h2{margin-top:40px;font-size:38px;font-weight:700}
.testimonials p{margin-top:6px;font-size:18px}
</style>
</head>
<body>
<header>
  <div class="brand"><span class="brand-dot"></span><span class="brand-name">Keyvale.com.au</span></div>
  <nav class="nav">
    <a style="left:609px">HOME</a>
    <a style="left:663px">FIXED FEES</a>
    <a style="left:740px">ARTICLES</a>
    <a style="left:807px">COMPANY</a>
    <a style="left:884px">CONTACT</a>
    <a style="left:961px">SIGN UP!</a>
    <a class="cart" style="left:1044px" aria-label="Cart">
      <svg width="11" height="10" viewBox="0 0 11 10"><path d="M0 0h2l1 5h6l1.5-4H3" fill="none" stroke="#333" stroke-width="1.6"/><rect x="2.5" y="2" width="7" height="3" fill="#333"/><circle cx="4" cy="8.5" r="1.2" fill="#333"/><circle cx="8.5" cy="8.5" r="1.2" fill="#333"/></svg>
    </a>
  </nav>
</header>

<main>
  <div class="steps">
    <span style="left:6px">1. YOUR STATUS</span>
    <span class="current" style="left:171px">2. PROPERTY TYPE</span>
    <span style="left:342px">3. QUOTE EXTRAS</span>
  </div>

  <h1 class="question">I am buying a...</h1>

  <div class="option selected" style="left:274px">
    <svg width="66" height="60" viewBox="0 0 66 60"><path d="M6 28 L33 5 L60 28" fill="none" stroke="#fff" stroke-width="7" stroke-linecap="round" stroke-linejoin="round"/><path d="M14 25 V54 H52 V25" fill="none" stroke="#fff" stroke-width="7" stroke-linejoin="round"/></svg>
    <span class="label">HOUSE</span>
  </div>
  <div class="option" style="left:434px">
    <svg width="62" height="62" viewBox="0 0 62 62"><rect x="0" y="0" width="62" height="62" rx="4" fill="#06a6da"/><rect x="10" y="10" width="17" height="17" fill="#fff"/><rect x="35" y="10" width="17" height="17" fill="#fff"/><rect x="10" y="35" width="17" height="17" fill="#fff"/><rect x="35" y="35" width="17" height="17" fill="#fff"/></svg>
    <span class="label">UNIT</span>
  </div>
  <div class="option" style="left:592px">
    <svg width="64" height="62" viewBox="0 0 64 62"><path d="M32 2 C22 2 15 9 15 18 C15 30 32 44 32 44 C32 44 49 30 49 18 C49 9 42 2 32 2Z" fill="#06a6da"/><circle cx="32" cy="18" r="6" fill="#fff"/><path d="M2 58 L12 48 H52 L62 58Z" fill="none" stroke="#06a6da" stroke-width="4" stroke-linejoin="round"/></svg>
    <span class="label">LAND</span>
  </div>
  <div class="option" style="left:753px">
    <svg width="64" height="62" viewBox="0 0 64 62"><path d="M14 24 L32 8 L50 24 V42 H14Z" fill="#06a6da"/><rect x="27" y="30" width="10" height="12" fill="#fff"/><path d="M2 58 L12 48 H52 L62 58Z" fill="none" stroke="#06a6da" stroke-width="4" stroke-linejoin="round"/></svg>
    <span class="label">HOUSE &amp; LAND</span>
  </div>

  <div class="btn btn-back">BACK</div>
  <div class="btn btn-next">NEXT</div>
</main>

<section class="testimonials">
  <h2>Our Customers Love Us</h2>
  <p>Don’t Just Take Our Word For It, Read It From Them</p>
</section>
</body>
</html>
```